Pelmora Tours - Astronomy in the Kimberley

Pelmora Tours requires a web page to advertise astronomy tours in the East Kimberley, Australia. It needs the following tabs - Home, Tours, Astronomy Events, Gallery, Testimonials, Contacts.

It should target tourists to the Kimberley.
We are unsure of which colours to go with at the moment but we have included our logo if it helps.

It should be mobile and tablet friendly.

Target Market(s)

Families, +40, Tourist, hobby astronomists,

Industry/Entity Type

Events

Number of Pages Required

3 page

Colors
3377b5
ffffff

Requirements
Must have
• Home, Tours, Astronomy Events, Gallery, Calendar, Testimonials, Contacts.
• 'Pelmora Tours' logo
Nice to have
• Pictures of portable amateur telescopes. Pictures of Lake Kununurra or Wyndham.
Should not have
• Pictures of extremely large professional telescopes.

```html
<!DOCTYPE html>
<html lang="en">
<head>
<meta charset="utf-8">
<title>Pelmora Tours – Astronomy in the Kimberley</title>
<link href="https://fonts.googleapis.com/css2?family=Questrial&display=swap" rel="stylesheet">
<style>
:root{
  --blue:#3367ad;
  --title:#2d5f9f;
  --ink:#444;
  --dark:#262626;
  --footer:#2e2e2e;
  --white:#fff;
  --social-blue:#3b62a8;
  --social-sky:#2a9fe0;
  --social-black:#2b2b2b;
  --social-red:#d8362b;
}
*{margin:0;padding:0;box-sizing:border-box}
html,body{width:746px;height:1200px;overflow:hidden;background:#fff}
body{position:relative;font-family:"Questrial",sans-serif;color:var(--ink)}
.abs{position:absolute}
a{color:inherit;text-decoration:none}
h1,h2,h3,h4,h5{font-weight:normal}

/* header */
.brand{left:46px;top:14px;display:flex;align-items:center;gap:6px}
.brand-dot{width:22px;height:22px;border-radius:50%;background:var(--blue)}
.brand-name{font-size:15px;color:#4a4a4a;line-height:1}
.top-links{right:46px;top:11px;font-size:8px;color:#555}
.top-links span{margin:0 4px}
.connect{right:46px;top:38px;display:flex;align-items:center;gap:3px}
.connect-label{font-size:7px;color:var(--title);margin-right:4px;letter-spacing:.2px}
.social{width:19px;height:19px;border-radius:50%;box-shadow:inset 0 -2px 0 rgba(0,0,0,.15)}

/* hero */
.hero{left:0;top:84px;width:746px;height:274px;
  background:linear-gradient(180deg,#b9cad8 0%,#8fa6b6 12%,#6c8aa3 20%,#4f7595 30%,#5b7b96 40%,#6c6a66 52%,#4a4038 66%,#7a6b5c 78%,#5b5048 90%,#8a7c6c 100%)}
.dots{left:346px;top:335px;display:flex;gap:6px}
.dots i{width:9px;height:9px;border-radius:50%;background:#111;display:block}
.dots i:first-child{background:var(--blue)}
.nav{left:46px;top:72px;width:654px;height:27px;background:var(--blue);border-radius:3px;display:flex;align-items:center;padding-left:15px}
.nav a{color:#fff;font-size:8.3px;letter-spacing:.3px;margin-right:38px}
.search{position:absolute;right:8px;top:6px;width:108px;height:15px;background:#fff;border-radius:1px;font-size:6.5px;font-style:italic;color:#666;padding:4px 0 0 8px}
.search svg{position:absolute;right:4px;top:3px}

/* welcome */
.welcome{left:53px;top:380px;width:640px;text-align:center}
.sec-title{font-size:14.5px;color:var(--title);letter-spacing:.3px}
.welcome p{font-size:7.4px;line-height:12.8px;margin-top:11px}
.btn{display:inline-block;background:var(--dark);color:#fff;font-size:7.2px;letter-spacing:.3px;text-align:center;border-radius:1px}
.welcome .btn{position:absolute;left:285px;top:91px;width:71px;height:23px;line-height:23px}

/* featured */
.featured{left:0;top:510px;width:746px;height:247px;background:var(--blue)}
.featured .sec-title{position:absolute;left:46px;top:23px;color:#fff}
.card{position:absolute;top:52px;width:151px}
.photo{display:block;width:151px;height:78px}
.card h3{color:#fff;font-size:10.5px;margin-top:9px}
.card p{color:#e6eefa;font-size:7.1px;line-height:12.6px;margin-top:1px}
.card .btn{margin-top:10px;width:71px;height:23px;line-height:23px}

/* astronomy tours */
.astro-title{left:46px;top:777px}
.arrows{left:666px;top:778px}
.astro-photo{left:46px;top:810px;width:151px;height:92px}
.astro-body{left:213px;top:807px;width:488px}
.astro-body h4{color:var(--title);font-size:9px}
.astro-body p{font-size:7.2px;line-height:12.8px;margin-top:2px}
.astro-body .btn{margin-top:7px;width:71px;height:23px;line-height:23px}

/* info band */
.info{left:0;top:928px;width:746px;height:201px;background:var(--blue)}
.info .sec-title{color:#fff}
.gallery{position:absolute;left:46px;top:24px}
.thumbs{display:grid;grid-template-columns:repeat(3,77px);gap:10px;margin-top:9px}
.thumbs div{height:56px}
.events{position:absolute;left:328px;top:24px;width:192px;color:#e7eefa}
.event{margin-top:8px}
.event + .event{border-top:1px solid #1d3e6b;margin-top:8px;padding-top:8px}
.event .date{font-size:8.5px;color:#fff}
.event p{font-size:7.2px;line-height:12.8px;margin-top:2px}
.event .more{font-size:6.8px;margin-top:2px}
.testi{position:absolute;left:550px;top:24px;width:146px;color:#e7eefa}
.testi p{font-style:italic;font-size:7.2px;line-height:12.8px;margin-top:8px;text-indent:10px}
.testi .who{font-size:6.8px;margin-top:8px}
.testi .btn{margin-top:17px;width:71px;height:23px;line-height:23px}

/* footer */
.footer{left:0;top:1129px;width:746px;height:71px;background:var(--footer)}
.foot-nav{position:absolute;left:46px;top:20px;font-size:8.2px;color:#ddd}
.foot-nav a{margin-right:17px}
.copy{position:absolute;left:46px;top:41px;font-size:6.8px;color:#5e5e5e}
.news{position:absolute;left:534px;top:16px}
.news h5{color:#fff;font-size:10.5px}
.news-form{margin-top:5px;width:166px;height:23px;background:#fff;display:flex;align-items:center;padding:0 2px 0 8px;font-size:6.5px;color:#777}
.news-form span{flex:1}
.news-form b{font-weight:normal;background:var(--blue);color:#fff;width:43px;height:19px;line-height:19px;text-align:center;font-size:6.8px}
</style>
</head>
<body>

<header>
  <div class="abs brand"><span class="brand-dot"></span><span class="brand-name">Pelmora Tours</span></div>
  <div class="abs top-links"><a href="#">Log In</a><span>|</span><a href="#">Register</a><span>|</span><a href="#">Site Map</a></div>
  <div class="abs connect"><span class="connect-label">CONNECT US:</span>
    <span class="social" style="background:var(--social-blue)"></span>
    <span class="social" style="background:var(--social-sky)"></span>
    <span class="social" style="background:var(--social-black)"></span>
    <span class="social" style="background:var(--social-red)"></span>
    <span class="social" style="background:var(--social-red)"></span>
    <span class="social" style="background:var(--social-red)"></span>
  </div>
</header>

<div class="abs hero" role="img" aria-label="Tourists gathered on a rocky lookout above a bay, gazing through binoculars"></div>
<div class="abs dots"><i></i><i></i><i></i><i></i></div>

<nav class="abs nav">
  <a href="#">HOME</a><a href="#">TOURS</a><a href="#">ASTRONOMY EVENTS</a><a href="#">GALLERY</a><a href="#">TESTIMONIALS</a><a href="#">CONTACTS</a>
  <div class="search">Search...
    <svg width="10" height="10" viewBox="0 0 10 10"><circle cx="4" cy="4" r="3" fill="none" stroke="#222" stroke-width="1.3"/><line x1="6.2" y1="6.2" x2="9.3" y2="9.3" stroke="#222" stroke-width="1.6"/></svg>
  </div>
</nav>

<section class="abs welcome">
  <h1 class="sec-title">WELCOME TO&nbsp; OUR WEBSITE</h1>
  <p>Aliquam molestie, mi et imperdiet euismod, dui purus auctor tellus, et interdum lacus lectus et ante. Sed accumsan sollicitudin sapien, sit amet adipiscing turpis gravida ac. In congue, neque ac lobortis volutpat, libero mauris varius mi, vitae suscipit ipsum ligula vitae risus. Duis aliquam nibh a dui iaculis viverra id a velit. Vivamus egestas risus in magna varius commodo. Sed semper viverra egestas. Etiam pretium porttitor lectus, vel ornare neque porta volutpat. Aenean a nibh eget turpis vehicula tempus ac sed massa. Vestibulum dolor nulla, ultrices ac tincidunt sed, laoreet non est.</p>
  <a class="btn" href="#">READ MORE</a>
</section>

<section class="abs featured">
  <h2 class="sec-title">FEATURED TOURS</h2>
  <div class="card" style="left:46px">
    <div class="photo" role="img" aria-label="Canal city skyline at sunset" style="background:linear-gradient(180deg,#5a6a88 0%,#c9884a 35%,#f2b04c 50%,#8a5a34 65%,#3a2820 100%)"></div>
    <h3>Heading Title</h3><p>Aliquam molestie, mi et imperdiet euismod, dui purus auctor tellus, et interdum lacus lectus et ante.</p>
    <a class="btn" href="#">VIEW DETAILS</a>
  </div>
  <div class="card" style="left:213px">
    <div class="photo" role="img" aria-label="Silhouette with a portable telescope under the Milky Way" style="background:linear-gradient(120deg,#0a0e1c 0%,#1c2850 35%,#5a6a9a 55%,#22305a 72%,#06080f 100%)"></div>
    <h3>Heading Title</h3><p>Aliquam molestie, mi et imperdiet euismod, dui purus auctor tellus, et interdum lacus lectus et ante.</p>
    <a class="btn" href="#">VIEW DETAILS</a>
  </div>
  <div class="card" style="left:382px">
    <div class="photo" role="img" aria-label="Visitors at a harbour viewpoint with city skyline" style="background:linear-gradient(180deg,#6aa0da 0%,#a8c8e8 30%,#8a98a8 48%,#c8b8a8 62%,#6a7884 80%,#4a525a 100%)"></div>
    <h3>Heading Title</h3><p>Aliquam molestie, mi et imperdiet euismod, dui purus auctor tellus, et interdum lacus lectus et ante.</p>
    <a class="btn" href="#">VIEW DETAILS</a>
  </div>
  <div class="card" style="left:550px">
    <div class="photo" role="img" aria-label="Crowd of tourists on a coastal lookout" style="background:linear-gradient(180deg,#5a98d8 0%,#8ab8e0 28%,#4a80b0 45%,#6a7a8a 60%,#8a7a68 78%,#5a4c40 100%)"></div>
    <h3>Heading Title</h3><p>Aliquam molestie, mi et imperdiet euismod, dui purus auctor tellus, et interdum lacus lectus et ante.</p>
    <a class="btn" href="#">VIEW DETAILS</a>
  </div>
</section>

<h2 class="abs sec-title astro-title">ASTRONOMY TOURS</h2>
<svg class="abs arrows" width="36" height="16" viewBox="0 0 36 16"><polyline points="8,2 2,8 8,14" fill="none" stroke="#333" stroke-width="1.4"/><polyline points="28,2 34,8 28,14" fill="none" stroke="#333" stroke-width="1.4"/></svg>
<div class="abs astro-photo" role="img" aria-label="Family looking through coin-operated viewing binoculars" style="background:linear-gradient(180deg,#6a9ed6 0%,#9cc0e4 30%,#7890a8 48%,#8a6a7a 62%,#4a4a58 80%,#6a5a4a 100%)"></div>
<div class="abs astro-body">
  <h4>Nam fermentum vestibulum purus</h4>
  <p>Aliquam molestie, mi et imperdiet euismod, dui purus auctor tellus, et interdum lacus lectus et ante. Sed accumsan sollicitudin sapien, sit amet adipiscing turpis gravida ac. In congue, neque ac lobortis volutpat, libero mauris varius mi, vitae suscipit ipsum ligula vitae risus. Duis aliquam nibh a dui iaculis viverra id a velit. Vivamus egestas risus in magna varius commodo. Sed semper viverra egestas. Etiam pretium porttitor lectus, vel ornare neque porta volutpat.</p>
  <a class="btn" href="#">READ MORE</a>
</div>

<section class="abs info">
  <div class="gallery">
    <h2 class="sec-title">GALLERY</h2>
    <div class="thumbs">
      <div role="img" aria-label="Child at a telescope" style="background:linear-gradient(135deg,#5a8ec0 0%,#a8b8c8 40%,#d89a70 65%,#8a5a48 100%)"></div>
      <div role="img" aria-label="Group under a starry sky" style="background:linear-gradient(180deg,#060a1c 0%,#1a2450 50%,#3a3a6a 75%,#1a1a2a 100%)"></div>
      <div role="img" aria-label="Coastal village at dusk" style="background:linear-gradient(180deg,#5a9ad8 0%,#a8c8e8 40%,#e8d8c8 60%,#d88a60 80%,#8a5040 100%)"></div>
      <div role="img" aria-label="Viewing binoculars over a city" style="background:linear-gradient(180deg,#7ab0e0 0%,#b8d0e8 35%,#8a8e94 55%,#5a5a5e 80%,#8a7a6a 100%)"></div>
      <div role="img" aria-label="Waterfront domed church" style="background:linear-gradient(180deg,#5a9ae0 0%,#c8b898 40%,#8a7a6a 55%,#3a9ab0 75%,#2a7a90 100%)"></div>
      <div role="img" aria-label="Harbour with boats" style="background:linear-gradient(180deg,#7ab4e4 0%,#d8a888 40%,#b06048 60%,#3a6aa0 80%,#2a4a80 100%)"></div>
    </div>
  </div>

  <div class="events">
    <h2 class="sec-title">ASTRONOMY EVENTS</h2>
    <div class="event"><div class="date">Mar 04 ,2015</div><p>Aliquam molestie, mi et imperdiet euismod, dui purus auctor tellus, et interdum lacus lectus et ante. ...</p><div class="more">Read More »</div></div>
    <div class="event"><div class="date">Mar 04 ,2015</div><p>Aliquam molestie, mi et imperdiet euismod, dui purus auctor tellus, et interdum lacus lectus et ante. ...</p><div class="more">Read More »</div></div>
  </div>

  <div class="testi">
    <h2 class="sec-title">TESTIMONIALS</h2>
    <p>Aliquam molestie, mi et imperdiet euismod, dui purus auctor tellus, et interdum lacus lectus et ante. Sed accumsan sollicitudin sapien, sit amet adipiscing turpis gravida ac. In congue..</p>
    <div class="who">- Name Goes Here</div>
    <a class="btn" href="#">READ ALL</a>
  </div>
</section>

<footer class="abs footer">
  <div class="foot-nav"><a href="#">Home</a><a href="#">Tours</a><a href="#">Astronomy Events</a><a href="#">Gallery</a><a href="#">Testimonials</a><a href="#">Contacts</a></div>
  <div class="copy">Copyright © 2015, CompanyName.All Right Reserved</div>
  <div class="news">
    <h5>Newsletter SignUp</h5>
    <div class="news-form"><span>Enter Email Address</span><b>SIGN UP</b></div>
  </div>
</footer>

</body>
</html>
```